Retail Jewelry Business Card Design Project

We are in need of a new business card design for a retail jewelry store. This store is in the business of fine jewelry including but not specific to bridal jewelry, diamonds, designer jewelry and watches.

This store has been in business for 20 years but continues to strive for a modern professional appeal. The main colors use for this business are a royal blue, white and silver.

Target Market(s)

Target market is ages 18-50

Industry/Entity Type

Jewelry

Requirements
Must have
• Sales Person Name
Sales Person Email Address

Store Address
Store Phone
Website

Standard business card size. No odd shapes or sizes.
Nice to have
• Overall modern feel for card.

We have thought that a design with a nice feature of the logo on the back of the card would be nice but open to ideas.
Should not have
• No specific images of jewelry should be used.

```html
<!DOCTYPE html>
<html lang="en">
<head>
<meta charset="utf-8">
<title>Harlow Lane Fine Jewelry – Business Card</title>
<link rel="stylesheet" href="https://fonts.googleapis.com/css2?family=Cinzel:wght@500&family=Open+Sans:wght@400;600&display=swap">
<style>
  :root {
    --royal-blue: #2e3a9c;
    --royal-blue-deep: #1c2470;
    --royal-blue-light: #3c4ab8;
    --silver: #d9dce4;
    --paper: #ffffff;
    --ink-grey: #4a4d5a;
    --backdrop: #e6e7eb;
  }
  * { box-sizing: border-box; margin: 0; padding: 0; }
  html, body {
    width: 1200px;
    height: 900px;
    overflow: hidden;
    background: var(--backdrop);
  }
  .canvas {
    position: relative;
    width: 1200px;
    height: 900px;
  }
  .card {
    position: absolute;
    left: 250px;
    width: 700px;
    height: 400px;
    border-radius: 4px;
    overflow: hidden;
    box-shadow: 0 6px 18px rgba(0, 0, 0, 0.18);
  }

  /* Back of card */
  .card--back {
    top: 40px;
    background: radial-gradient(ellipse at 50% 45%, var(--royal-blue-light) 0%, var(--royal-blue) 45%, var(--royal-blue-deep) 100%);
    display: flex;
    align-items: center;
    justify-content: center;
  }
  .brand-name--back {
    font-family: "Cinzel", serif;
    font-weight: 500;
    font-size: 50px;
    letter-spacing: 3px;
    color: var(--silver);
    text-align: center;
    line-height: 1.2;
  }

  /* Front of card */
  .card--front {
    top: 460px;
    background: var(--paper);
  }
  .brand-name--front {
    position: absolute;
    top: 44px;
    left: 280px;
    width: 380px;
    font-family: "Cinzel", serif;
    font-weight: 500;
    font-size: 34px;
    letter-spacing: 2px;
    line-height: 1.2;
    color: var(--royal-blue);
    text-align: center;
  }
  .contact {
    position: absolute;
    top: 160px;
    left: 230px;
    width: 420px;
    text-align: center;
    font-family: "Open Sans", sans-serif;
    color: var(--ink-grey);
    font-size: 15px;
    line-height: 1.55;
  }
  .contact__name {
    font-weight: 600;
    font-size: 19px;
    letter-spacing: 0.5px;
    color: var(--royal-blue);
    text-transform: uppercase;
    margin-bottom: 4px;
  }
  .footer-band {
    position: absolute;
    left: 0;
    bottom: 0;
    width: 100%;
    height: 88px;
    background: var(--royal-blue);
    display: flex;
    align-items: center;
    padding-left: 36px;
  }
  .footer-band__web {
    font-family: "Open Sans", sans-serif;
    font-size: 16px;
    color: var(--paper);
    letter-spacing: 0.3px;
  }
</style>
</head>
<body>
  <main class="canvas">
    <section class="card card--back" aria-label="Card back">
      <p class="brand-name--back">Harlow Lane<br>Fine Jewelry</p>
    </section>

    <section class="card card--front" aria-label="Card front">
      <p class="brand-name--front">Harlow Lane<br>Fine Jewelry</p>
      <div class="contact">
        <p class="contact__name">Ellis Harlow Whitmore</p>
        <p class="contact__email">ellis@harlowlanejewelry.com</p>
        <p class="contact__phone">555 555 0148</p>
        <p class="contact__address">2270 Marlowe Avenue Bayport, FL 32590</p>
      </div>
      <div class="footer-band">
        <p class="footer-band__web">www.HarlowLaneJewelry.com</p>
      </div>
    </section>
  </main>
</body>
</html>
```